Youth basketball program needs a one sided flyer to recruit new players for our competitive teams

We need a flyer to recruit players for our competitive youth basketball teams. Our program is "Lakeshore Ember Basketball" (see www.lsember.example); we are a nonprofit organization that provides opportunities to participate in youth basketball. We are focused on player development (improving each player's fundamentals and related skills.)

We are currently looking for skilled players that will be in the following grades next school year: boys 5th and 6th grade, girls 7th grade. Tryouts will occur in June - July for next season's teams. Girls season goes from October - December (break during January and February so players can play on their school teams) and March - mid April. Boys season goes from November - mid March. Interested players need to contact us to arrange a try out. During the season, teams will practice each week and play in local/regional leagues and tournaments.

We have partnered with Dorian Kessler Basketball Training (see his website at: http://www.dkhoopgrow.example/#!about/citr ) to provide training sessions for all our players.

We would like the following items included in the flyer: our LEB logo, reference to Dorian Kessler and the colors of green & white. The final design should emphasize our focus on player development.

Reason: Designers - thanks for the submissions thus far! I'm currently traveling abroad and haven't been able to provide adequate feedback so I'm going to extend the deadline to allow time for this. Thanks!!

Designers - thank you for all the submissions!  We were very impressed with the creativity and professionalism..  Unfortunately, we can only select one design and we have settled on the flyer/design. Thanks again for your efforts.  - Lakeshore Ember team

Target Market(s)

Boys ages 9-12, girls ages 11-13 and their respective parents.

Industry/Entity Type

Training

Requirements
Must have
• The flyer must include our Lakeshore Ember Basketball logo (can either be the colored logo or the green/white logo), our website address and the Twitter & Facebook logos to direct individuals to our web locations.

```html
<!DOCTYPE html>
<html lang="en">
<head>
<meta charset="utf-8">
<title>Lakeshore Ember Basketball – Tryouts</title>
<link href="https://fonts.googleapis.com/css2?family=Oswald:wght@500&family=Spinnaker&family=Alegreya:wght@400&display=swap" rel="stylesheet">
<style>
  :root {
    --frame: #ececec;
    --paper: #ffffff;
    --ember-green: #0f4434;
    --deep-green: #123f31;
    --shadow: #0a0a0a;
    --ball-orange: #e2822f;
    --photo-warm: #b9a898;
    --photo-dark: #3b4a40;
  }
  * { margin: 0; padding: 0; box-sizing: border-box; }
  html, body { width: 936px; height: 1200px; overflow: hidden; }
  body { background: var(--frame); position: relative; }
  .flyer {
    position: absolute; left: 18px; top: 18px; width: 900px; height: 1164px;
    background: var(--paper); overflow: hidden;
  }
  .team-photo {
    position: absolute; left: 0; top: 0; width: 900px; height: 390px;
    background: linear-gradient(180deg, #d8d2c8 0%, var(--photo-warm) 35%, var(--photo-dark) 80%, #2c3a31 100%);
  }
  .brand-band {
    position: absolute; left: 0; top: 390px; width: 900px; height: 180px;
    background: var(--paper);
  }
  .brand-mark {
    position: absolute; left: 53px; top: 14px; width: 164px; height: 164px;
    border-radius: 50%; background: var(--ball-orange);
    display: flex; align-items: center; justify-content: center; text-align: center;
    font-family: 'Oswald', sans-serif; font-weight: 500; font-size: 22px; line-height: 1.1;
    color: var(--ember-green); text-transform: uppercase; padding: 0 18px;
  }
  .brand-title {
    position: absolute; left: 276px; top: 60px; width: 600px;
    font-family: 'Oswald', sans-serif; font-weight: 500; color: var(--ember-green);
    text-transform: uppercase; text-align: center; line-height: 1;
  }
  .brand-title h1 { font-size: 36px; font-weight: 500; letter-spacing: 0.5px; }
  .brand-title .site { display: block; font-size: 23px; margin-top: 6px; }
  .fade-photo {
    position: absolute; left: 0; top: 570px; width: 900px; height: 140px;
    background: linear-gradient(180deg, #d9cfc4 0%, #efe9e3 45%, var(--paper) 100%);
  }
  .info-card {
    position: absolute; left: 149px; top: 594px; width: 604px; height: 466px;
    background: var(--deep-green);
    box-shadow: 9px 9px 0 var(--shadow);
    padding: 30px 28px;
  }
  .info-card p {
    font-family: 'Spinnaker', sans-serif; color: #fff; text-transform: uppercase;
    font-size: 20.5px; line-height: 28px; text-align: justify; letter-spacing: 1px;
    font-weight: 700;
  }
  .partner-note {
    position: absolute; left: 0; top: 1094px; width: 900px; text-align: center;
    font-family: 'Alegreya', serif; font-size: 18px; line-height: 26px; color: var(--ember-green);
  }
</style>
</head>
<body>
  <main class="flyer">
    <div class="team-photo" role="img" aria-label="Photo of a youth girls basketball team in green and white uniforms huddled with their coach"></div>

    <header class="brand-band">
      <div class="brand-mark">Lakeshore Ember</div>
      <div class="brand-title">
        <h1>Lakeshore Ember Basketball</h1>
        <span class="site">www.lsember.example</span>
      </div>
    </header>

    <div class="fade-photo" role="img" aria-label="Faded gym background photo"></div>

    <section class="info-card">
      <p>We are currently looking for skilled players that will be in the following grades next school year: boys 5th and 6th grade, girls 7th grade. Tryouts will occur in June - July for next season's teams. Girls season goes from October - December (break during January and February so players can play on their school teams) and March - mid April. Boys season goes from November - mid March. Interested players need to contact us to arrange a try out. During the season, teams will practice each week and play in local/regional leagues and tournaments</p>
    </section>

    <p class="partner-note">We have partnered with Dorian Kessler Basketball Training<br>to provide training sessions for all our players.</p>
  </main>
</body>
</html>
```